Brochure Design For Beauty Salon

We have an existing brochure for our beauty salon business which has been designed in-house.

We need a designer to refresh the look and feel of the brochure, which is intended for print. The print format will be 210mmx210mm (square, stapled).

We need a design for each and every page of the brochure, including the front and back covers.

We are looking for a fresh modern design, quite close to what we already have, but looking more slick and professional.

The primary colors are white, grey and purple. The final design will communicate luxury, prestige and cleanliness and have a heavy focus on creating the feeling of space within each page.

Target Market(s)

Professional Women, aged 20-45

Industry/Entity Type

Beauty Salon

Font styles to use
Sans Serif
Other font styles liked:
• Helvetica

Requirements
Must have
• The project must be ready for print on square paper 210x210mm

```html
<!DOCTYPE html>
<html lang="en">
<head>
<meta charset="utf-8">
<title>Luna Lux – Facials Menu Spread</title>
<link href="https://fonts.googleapis.com/css2?family=Open+Sans:wght@300;400;600;700&display=swap" rel="stylesheet">
<style>
  :root{
    --plum:#5a1336;
    --plum-dark:#45102a;
    --ink:#3d3d3d;
    --grey:#6f6f6f;
    --rule-grey:#8a8a8a;
    --paper:#f7f7f7;
    --backdrop:#d9d9de;
  }
  *{box-sizing:border-box;margin:0;padding:0}
  html,body{width:1200px;height:730px;overflow:hidden}
  body{background:var(--backdrop);font-family:"Open Sans",Arial,sans-serif;color:var(--ink);position:relative}
  .spread{position:absolute;left:60px;top:95px;width:1080px;height:540px;display:flex;box-shadow:0 10px 30px rgba(0,0,0,.18)}
  .page{position:relative;width:540px;height:540px;background:var(--paper);overflow:hidden}
  .page--left{border-right:1px solid #e2e2e2}
  .section-title{position:absolute;display:flex;align-items:center;gap:10px;font-weight:300;font-size:22px;letter-spacing:1px;color:var(--ink);text-transform:uppercase}
  .section-title strong{font-weight:700;color:var(--plum);letter-spacing:.5px}
  .section-title .title-rule{height:1px;background:var(--plum);flex:1}
  .intro{position:absolute;font-size:11.5px;line-height:1.45;color:var(--grey);font-weight:300;letter-spacing:.4px}
  .treatment{position:absolute;left:40px;right:40px}
  .treatment-head{display:flex;justify-content:space-between;align-items:flex-end}
  .treatment-name{font-size:14px;color:var(--ink);font-weight:400}
  .treatment-price{font-size:14px;font-weight:700;color:var(--plum)}
  .treatment-rule{display:block;width:100%;height:6px;margin:2px 0 4px}
  .treatment-desc{font-size:8.5px;line-height:1.4;color:var(--grey)}
  .photo{position:absolute;left:0;top:255px;width:540px;height:240px;
    background:linear-gradient(180deg,#f3f1ef 0%,#e9e4e0 45%,#dcd2cb 70%,#efeceb 100%)}
  .footer{position:absolute;left:0;bottom:0;width:540px;height:80px}
  .footer svg{position:absolute;left:0;top:0}
  .footer-url{position:absolute;left:0;right:0;bottom:16px;text-align:center;color:#fff;font-size:13px;font-weight:300;letter-spacing:.3px}
  .footer-url b{font-weight:700}
</style>
</head>
<body>
<div class="spread">
  <!-- Left page -->
  <section class="page page--left">
    <h2 class="section-title" style="left:40px;right:30px;top:40px">Clarivel <strong>Facials</strong><span class="title-rule"></span></h2>
    <p class="intro" style="left:40px;right:40px;top:82px">The results you are going to see with a Clarivel skin treatment are unlike anything else in the industry because we exfoliate the skin, we double cleanse the skin, we do extractions, tailor-made customized massage and masque technique.</p>
    <div class="treatment" style="top:140px">
      <div class="treatment-head"><span></span><span class="treatment-price">£10 | 10 mins</span></div>
      <svg class="treatment-rule" viewBox="0 0 460 6" preserveAspectRatio="none"><path d="M0 5 Q230 -1 460 1 L460 1.6 Q230 1 0 6 Z" fill="var(--plum)"/></svg>
      <div class="treatment-name" style="font-size:15px;font-weight:300;letter-spacing:.5px">Skin Reset</div>
      <svg class="treatment-rule" viewBox="0 0 460 6" preserveAspectRatio="none"><path d="M0 5 L150 4 L150 6 L0 6 Z" fill="var(--plum)"/><path d="M150 4.5 L460 2 L460 2.6 L150 5.2 Z" fill="var(--rule-grey)"/></svg>
      <p class="treatment-desc" style="font-size:9px;font-style:italic">Test-drive your prescribed regimen under the guidance of a professional Skin Therapist. At Skin Studio, you can learn about your skin with Skin Charting and then learn how to use the products, hands-on.</p>
    </div>
    <div class="photo" role="img" aria-label="Photo of a client relaxing with a clay face masque applied by a therapist's brush"></div>
    <div class="footer">
      <svg width="540" height="80" viewBox="0 0 540 80"><path d="M0 22 Q270 6 540 14 L540 80 L0 80 Z" fill="#6b6b6b"/><path d="M0 28 Q270 12 540 20 L540 80 L0 80 Z" fill="#fff"/><path d="M0 32 Q270 16 540 24 L540 80 L0 80 Z" fill="var(--plum)"/></svg>
      <div class="footer-url">www.<b>lunalux</b>.co.uk</div>
    </div>
  </section>

  <!-- Right page -->
  <section class="page page--right">
    <h2 class="section-title" style="left:40px;right:60px;top:38px">Signature <strong>Facials</strong><span class="title-rule"></span></h2>
    <p class="intro" style="left:40px;right:40px;top:78px;font-weight:400;font-size:10px;color:var(--ink)">Deep cleansing and ultra hydrating, our signature facials are tailor made for your skin.</p>

    <div class="treatment" style="top:100px">
      <div class="treatment-head"><span class="treatment-name">Microfocus Signature Facial</span><span class="treatment-price">£35 | 30 mins</span></div>
      <svg class="treatment-rule" viewBox="0 0 460 6" preserveAspectRatio="none"><path d="M0 5 L140 4 L140 6 L0 6 Z" fill="var(--plum)"/><path d="M140 4.5 L460 3 L460 3.6 L140 5.2 Z" fill="var(--plum-dark)"/></svg>
      <p class="treatment-desc">We focus on key stages of treatment to get your maximum results in a minimum of time.</p>
    </div>
    <div class="treatment" style="top:158px">
      <div class="treatment-head"><span class="treatment-name">Luna Lux Signature Facial</span><span class="treatment-price">£55 | 60 mins</span></div>
      <svg class="treatment-rule" viewBox="0 0 460 6" preserveAspectRatio="none"><path d="M0 5 L140 4 L140 6 L0 6 Z" fill="var(--plum)"/><path d="M140 4.5 L460 3 L460 3.6 L140 5.2 Z" fill="var(--plum-dark)"/></svg>
      <p class="treatment-desc">A bespoke facial customised at every stage.</p>
    </div>
    <div class="treatment" style="top:216px">
      <div class="treatment-head"><span class="treatment-name">Luxury Signature Facial</span><span class="treatment-price">£85 | 90 mins</span></div>
      <svg class="treatment-rule" viewBox="0 0 460 6" preserveAspectRatio="none"><path d="M0 5 L140 4 L140 6 L0 6 Z" fill="var(--plum)"/><path d="M140 4.5 L460 3 L460 3.6 L140 5.2 Z" fill="var(--plum-dark)"/></svg>
      <p class="treatment-desc">Upgrade to the luxury facial and enjoy a deeply hydrating masque and soothing touch therapy.</p>
    </div>

    <h2 class="section-title" style="left:40px;right:40px;top:272px">Eye <strong>Lift</strong><span class="title-rule"></span></h2>

    <div class="treatment" style="top:312px">
      <div class="treatment-head"><span class="treatment-name">Eyelift Microfocus Facial</span><span class="treatment-price">£35 | 30 mins</span></div>
      <svg class="treatment-rule" viewBox="0 0 460 6" preserveAspectRatio="none"><path d="M0 5 L140 4 L140 6 L0 6 Z" fill="var(--plum)"/><path d="M140 4.5 L460 3 L460 3.6 L140 5.2 Z" fill="var(--plum-dark)"/></svg>
      <p class="treatment-desc">This intensive, energising professional treatment focuses on the eye area and delivers benefits including lymph drainage, reduced puffiness, fewer visible fine lines and brighter skin around the eyes.</p>
    </div>
    <div class="treatment" style="top:382px">
      <div class="treatment-head"><span class="treatment-name">Eyelift Add-on</span><span class="treatment-price">£15 | 15 mins</span></div>
      <svg class="treatment-rule" viewBox="0 0 460 6" preserveAspectRatio="none"><path d="M0 5 L140 4 L140 6 L0 6 Z" fill="var(--plum)"/><path d="M140 4.5 L460 3 L460 3.6 L140 5.2 Z" fill="var(--plum-dark)"/></svg>
      <p class="treatment-desc">This eye-opening service is to illuminate the eye area and promote an energised, positive appearance while the body is experiencing stress. It delivers quick, visible eye benefits. Add this 15 minute service to your regular facial.</p>
    </div>

    <div class="footer">
      <svg width="540" height="80" viewBox="0 0 540 80"><path d="M0 14 Q270 6 540 22 L540 80 L0 80 Z" fill="#6b6b6b"/><path d="M0 20 Q270 12 540 28 L540 80 L0 80 Z" fill="#fff"/><path d="M0 24 Q270 16 540 32 L540 80 L0 80 Z" fill="var(--plum)"/></svg>
      <div class="footer-url">www.<b>lunalux</b>.co.uk</div>
    </div>
  </section>
</div>
</body>
</html>
```